731 Orchard Avenue Residences

designing a sign for apartment complex;
prefer colors gray white and yellow

Target Market(s)

residents coming home to their apartment

Font styles to use
Serif
Sans Serif

Colors
FFF300
FFF600
FEFA6F
FFFEC7
FFFEE8

Requirements
Must have
• black or gray, white and some yellow; easy to read and see

```html
<!DOCTYPE html>
<html lang="en">
<head>
<meta charset="utf-8">
<title>731 Orchard Avenue Residences – Sign</title>
<link rel="stylesheet" href="https://fonts.googleapis.com/css2?family=Abril+Fatface&display=swap">
<style>
  :root {
    --page-white: #ffffff;
    --sign-black: #1b1b1b;
    --sign-black-soft: #2a2a2a;
    --sign-yellow: #ffd600;
    --sign-yellow-soft: #f0c800;
    --frame-gold: #ffd600;
    --frame-black: #111111;
    --text-black: #050505;
  }
  html, body {
    margin: 0;
    padding: 0;
    width: 1200px;
    height: 900px;
    overflow: hidden;
    background: var(--page-white);
  }
  .sign {
    position: absolute;
    left: 18px;
    top: 0;
    width: 1164px;
    height: 900px;
    font-family: "Abril Fatface", Georgia, serif;
  }
  .band {
    position: absolute;
    left: 0;
    width: 1164px;
  }
  .band--upper {
    top: 0;
    height: 463px;
    background:
      radial-gradient(circle at 30% 40%, var(--sign-black-soft) 0%, transparent 60%),
      radial-gradient(circle at 80% 70%, var(--sign-black-soft) 0%, transparent 55%),
      var(--sign-black);
  }
  .band--lower {
    top: 463px;
    height: 437px;
    background:
      radial-gradient(circle at 25% 60%, var(--sign-yellow-soft) 0%, transparent 60%),
      radial-gradient(circle at 85% 30%, var(--sign-yellow-soft) 0%, transparent 55%),
      var(--sign-yellow);
  }
  .artwork {
    position: absolute;
    inset: 0;
  }
  .house-number {
    font-size: 300px;
    letter-spacing: 4px;
    fill: var(--sign-yellow);
  }
  .building-name {
    font-size: 104px;
    letter-spacing: 3px;
    fill: var(--text-black);
  }
</style>
</head>
<body>
  <main class="sign">
    <div class="band band--upper" role="img" aria-label="Dark charcoal field with a subtle interlocking swirl pattern"></div>
    <div class="band band--lower" role="img" aria-label="Yellow field with a subtle interlocking swirl pattern"></div>

    <svg class="artwork" width="1164" height="900" viewBox="0 0 1164 900">
      <polyline points="26,463 26,26 1138,26 1138,463" fill="none" stroke="var(--frame-gold)" stroke-width="2.5"/>
      <polyline points="26,463 26,874 1138,874 1138,463" fill="none" stroke="var(--frame-black)" stroke-width="2.5"/>
      <text class="house-number" x="166" y="399">731</text>
      <text class="building-name" x="166" y="590">Orchard Avenue</text>
      <text class="building-name" x="166" y="718">Residences</text>
    </svg>
  </main>
</body>
</html>
```